Past Cedar Hills Oz Tour Flyer

I need a dynamic flyer for a concert tour.
I have uploaded the file. Please use these ingredients for the design.
The font for the title is Jellyka Jellyfish lower case from www.glyphmarket-demo.net
Updates
We are getting close!! We just need bright colours, the headings to STAND OUT and Byron Bay has to be moved to under NSW Bellingen.
Thanks for all your hard work!
Target Market(s)
We are targeting a wide range of customers from old age to children and families
Industry/Entity Type
Tour
Look and feel
Each slider illustrates characteristics of the customer's brand and the style your logo design should communicate.

```html
<!DOCTYPE html>
<html lang="en">
<head>
<meta charset="utf-8">
<title>Past Cedar Hills – Australia Tour Flyer</title>
<link rel="stylesheet" href="https://fonts.googleapis.com/css2?family=Parisienne&family=Fira+Sans+Condensed:wght@400&family=Oswald:wght@400&family=Open+Sans:wght@400&display=swap">
<style>
  :root {
    --backdrop: #d9d9d9;
    --ink-black: #050505;
    --white: #ffffff;
    --orange: #e8801c;
    --tour-orange: #f08a2a;
    --heading-yellow: #f5e61a;
    --sky-purple: #5a2f6e;
    --sky-blue: #2a3f7a;
  }
  * { margin: 0; padding: 0; box-sizing: border-box; }
  html, body { width: 1200px; height: 954px; overflow: hidden; background: var(--backdrop); }
  .flyer {
    position: absolute; left: 310px; top: 58px; width: 580px; height: 838px;
    background: var(--ink-black); overflow: hidden;
    font-family: 'Open Sans', sans-serif; color: var(--white);
  }
  .flyer__photo {
    position: absolute; left: 0; top: 0; width: 580px; height: 460px;
    background:
      radial-gradient(ellipse 170px 260px at 420px 260px, rgba(230,110,40,.85), rgba(200,60,30,.35) 60%, transparent 100%),
      radial-gradient(ellipse 320px 200px at 150px 140px, rgba(150,90,60,.55), transparent 70%),
      linear-gradient(180deg, var(--sky-purple) 0%, var(--sky-blue) 35%, #120b18 80%, var(--ink-black) 100%);
  }
  .flyer__pattern {
    position: absolute; left: 0; top: 390px; width: 580px; height: 310px;
    background:
      radial-gradient(ellipse 160px 140px at 80px 180px, rgba(18,112,122,.9), transparent 75%),
      radial-gradient(ellipse 180px 150px at 230px 170px, rgba(200,32,58,.9), transparent 75%),
      radial-gradient(ellipse 160px 150px at 360px 150px, rgba(40,150,150,.7), transparent 75%),
      radial-gradient(ellipse 180px 160px at 500px 190px, rgba(30,106,68,.85), transparent 75%),
      linear-gradient(180deg, transparent 0%, rgba(0,0,0,.2) 100%);
    mask-image: linear-gradient(180deg, transparent 0%, #000 30%, #000 100%);
    -webkit-mask-image: linear-gradient(180deg, transparent 0%, #000 30%, #000 100%);
  }
  .title {
    position: absolute; left: 70px; top: 50px; width: 320px;
    font-family: 'Parisienne', cursive; font-weight: 400;
    font-size: 76px; line-height: 78px; text-transform: lowercase;
    color: var(--white);
  }
  .title__line2 { display: block; padding-left: 40px; }
  .subtitle {
    position: absolute; left: 0; top: 232px; width: 364px; text-align: center;
    font-family: 'Fira Sans Condensed', sans-serif; font-size: 26px; line-height: 32px;
  }
  .subtitle__tour { display: block; color: var(--tour-orange); margin-top: 6px; }
  .venues { position: absolute; font-size: 15px; line-height: 21.2px; }
  .venues__heading {
    font-family: 'Oswald', sans-serif; font-weight: 400; font-size: 24px; line-height: 30px;
    color: var(--heading-yellow); margin-bottom: 1px;
  }
  .venues__list { list-style: none; }
  .venues--vic { left: 85px; top: 458px; }
  .venues--act { left: 85px; top: 612px; }
  .venues--nsw { left: 218px; top: 458px; }
  .venues--qld { left: 381px; top: 512px; }
  .footer { position: absolute; left: 0; top: 700px; width: 580px; height: 138px; display: flex; }
  .footer__tickets {
    width: 290px; background: var(--orange); text-align: center;
    font-family: 'Fira Sans Condensed', sans-serif; font-size: 20px; line-height: 21px;
    padding-top: 16px;
  }
  .footer__partners {
    flex: 1; display: flex; align-items: center; justify-content: space-around;
    padding: 0 14px; font-size: 14px;
  }
  .partner { display: flex; align-items: center; gap: 7px; }
  .partner__mark { width: 12px; height: 12px; background: var(--orange); border-radius: 50%; }
  .partner__mark--square { border-radius: 0; background: var(--white); }
</style>
</head>
<body>
  <main class="flyer">
    <div class="flyer__photo" role="img" aria-label="Night-sky photo with bokeh lights and a young choir member dancing in a bright orange and yellow costume with a straw skirt"></div>
    <div class="flyer__pattern" role="img" aria-label="Colourful triangle mosaic pattern in teal, red and green"></div>

    <h1 class="title"><span>past cedar</span><span class="title__line2">hills</span></h1>
    <p class="subtitle">The Sunrise Youth Choir<span class="subtitle__tour">Australia Tour</span></p>

    <section class="venues venues--vic">
      <h2 class="venues__heading">VICTORIA</h2>
      <ul class="venues__list"><li>Geelong</li><li>Sunbury</li><li>Melbourne</li><li>Bendigo</li><li>Albury</li></ul>
    </section>
    <section class="venues venues--act">
      <h2 class="venues__heading">A.C.T.</h2>
      <ul class="venues__list"><li>Canberra</li></ul>
    </section>
    <section class="venues venues--nsw">
      <h2 class="venues__heading">N.S.W.</h2>
      <ul class="venues__list"><li>Nowra</li><li>Sydney</li><li>Wollongong</li><li>Blue Mountains</li><li>Port Macquarie</li><li>Laurieton</li><li>Taree</li><li>Bellingen</li><li>Byron Bay</li></ul>
    </section>
    <section class="venues venues--qld">
      <h2 class="venues__heading">QLD</h2>
      <ul class="venues__list"><li>Gold Coast</li><li>Sunshine Coast</li><li>Brisbane</li></ul>
    </section>

    <footer class="footer">
      <div class="footer__tickets">TICKETS and info at<br>www.choirtour-demo.org<br>CONTACT:<br>Dana Mirrow&nbsp; 0400 000 123</div>
      <div class="footer__partners">
        <div class="partner"><span class="partner__mark"></span><span>Chorus Link</span></div>
        <div class="partner"><span class="partner__mark partner__mark--square"></span><span>Sunrise Choir</span></div>
      </div>
    </footer>
  </main>
</body>
</html>
```